Report Design

I am looking for a redesign of our monthly inspection reports we submit to our customers. I uploaded the current one we use (Tallowfern) and also that of a competitor (Cedar Knoll). I want to more copy the layout of the Cedarknoll report I attached but with more flow and design.

Requirements
Must have
• This has to be in a template format that we can modify the content every month.

```html
<!DOCTYPE html>
<html lang="en">
<head>
<meta charset="utf-8">
<title>Landscape, Irr. &amp; Property Inspection – Tallowfern</title>
<link href="https://fonts.googleapis.com/css2?family=Hind:wght@300;400;600;700&display=swap" rel="stylesheet">
<style>
  :root {
    --green-dark: #006633;
    --green-light: #5ac24a;
    --ink: #1a1a1a;
    --paper: #ffffff;
  }
  * { margin: 0; padding: 0; box-sizing: border-box; }
  html, body { width: 848px; height: 1200px; overflow: hidden; background: var(--paper); }
  body { font-family: "Hind", Arial, sans-serif; color: var(--ink); position: relative; }

  .report-title {
    position: absolute; left: 49px; top: 52px;
    font-size: 24px; font-weight: 700; letter-spacing: -0.2px;
  }
  .property-band {
    position: absolute; left: 50px; top: 93px; width: 688px; height: 54px;
    background: var(--green-dark); color: var(--paper);
    font-size: 25px; font-weight: 700; line-height: 54px; padding-left: 12px;
  }
  .page-number {
    position: absolute; left: 753px; top: 93px; width: 51px; height: 54px;
    background: var(--green-light); color: var(--paper);
    font-size: 24px; font-weight: 700; text-align: center; line-height: 28px; padding-top: 3px;
  }
  .item-card {
    position: absolute; left: 50px; top: 169px; width: 753px; height: 425px;
    border: 1px solid var(--green-dark);
  }
  .item-heading {
    position: absolute; left: 20px; top: 25px;
    font-size: 17px; font-weight: 700; color: var(--green-dark);
  }
  .item-heading .num { margin-right: 8px; }
  .item-text {
    position: absolute; left: 22px; top: 54px;
    font-size: 15px; font-weight: 400;
  }
  .item-photo { position: absolute; top: 103px; width: 339px; height: 291px; }
  .item-photo.left { left: 22px; background: linear-gradient(160deg, #b9c3c9 0%, #7a8f6a 28%, #7d1b26 52%, #5a1419 78%, #3a2a22 100%); }
  .item-photo.right { left: 388px; background: linear-gradient(200deg, #a9b3ba 0%, #8c9090 35%, #9aa24a 55%, #6b1a22 78%, #2f241e 100%); }

  .footer-rule {
    position: absolute; left: 49px; top: 1080px; width: 756px; height: 0;
    border-top: 1.5px solid var(--green-dark);
  }
  .footer-title {
    position: absolute; left: 61px; top: 1100px;
    font-size: 20.5px; font-weight: 700;
  }
  .footer-division {
    position: absolute; left: 62px; top: 1128px;
    font-size: 15px; font-weight: 400; color: var(--green-dark);
  }
  .footer-contacts {
    position: absolute; left: 63px; top: 1155px;
    display: flex; align-items: center; font-size: 13px;
  }
  .contact { display: flex; align-items: center; margin-right: 24px; }
  .contact svg { width: 14px; height: 14px; margin-right: 8px; }
  .brand {
    position: absolute; left: 668px; top: 1128px;
    display: flex; align-items: center;
  }
  .brand-dot { width: 14px; height: 14px; border-radius: 50%; background: var(--green-light); margin-right: 8px; }
  .brand-name { font-size: 22px; font-weight: 700; color: var(--ink); }
</style>
</head>
<body>
  <header>
    <h1 class="report-title">Landscape, Irr. &amp; Property Inspection</h1>
    <div class="property-band">Gardens on Larkspur POA &amp; Retail</div>
    <div class="page-number">4</div>
  </header>

  <section class="item-card">
    <h2 class="item-heading"><span class="num">8.</span>Plants filling in:</h2>
    <p class="item-text">The copper plants and Jasmine are all filling in nicely</p>
    <div class="item-photo left" role="img" aria-label="Photo of a curved bed of red copper plants beside a sidewalk at the entrance"></div>
    <div class="item-photo right" role="img" aria-label="Photo of a staked palm in a median bed with copper plants and jasmine"></div>
  </section>

  <footer>
    <div class="footer-rule"></div>
    <div class="footer-title">Landscape, Irr. &amp; Property Inspection</div>
    <div class="footer-division">Landscape and Grounds Maintenance Division</div>
    <div class="footer-contacts">
      <span class="contact">
        <svg viewBox="0 0 14 14"><circle cx="7" cy="7" r="7" fill="#1a1a1a"/><path d="M4.3 3.6l1.4-.3.8 1.9-.9.7c.4.9 1.1 1.6 2 2l.7-.9 1.9.8-.3 1.4c-3.2.1-5.7-2.4-5.6-5.6z" fill="#fff"/></svg>
        352-555-0148
      </span>
      <span class="contact">
        <svg viewBox="0 0 14 14"><circle cx="7" cy="7" r="7" fill="#1a1a1a"/><rect x="4.5" y="3.5" width="5" height="3" fill="#fff"/><rect x="3.5" y="6.5" width="7" height="4" rx=".6" fill="#fff"/><rect x="5" y="8" width="4" height=".8" fill="#1a1a1a"/></svg>
        Fax 877-555-0193
      </span>
      <span class="contact">
        <svg viewBox="0 0 14 14"><circle cx="7" cy="7" r="7" fill="#1a1a1a"/><path d="M7 3a2.4 2.4 0 0 0-2.4 2.4C4.6 7.3 7 10.4 7 10.4s2.4-3.1 2.4-5A2.4 2.4 0 0 0 7 3z" fill="#fff"/><circle cx="7" cy="5.4" r=".9" fill="#1a1a1a"/></svg>
        1420 Harlow Road, Pine Hollow, FL 33599
      </span>
    </div>
    <div class="brand">
      <span class="brand-dot"></span>
      <span class="brand-name">Tallowfern</span>
    </div>
  </footer>
</body>
</html>
```